HarmoNest Ensemble Jubilee
Date: Sunday Oct 2, 2022
When: 2-4 p.m.
Location: Brindle9 Alehouse
413 Marlowe Ct #200, Sacramento, CA 95821
Tickets: www.Tixolvo.com
General seating: $15 for adults and $10 for students

```html
<!DOCTYPE html>
<html lang="en">
<head>
<meta charset="utf-8">
<title>HarmoNest Ensemble Jubilee</title>
<link rel="stylesheet" href="https://fonts.googleapis.com/css2?family=Kaushan+Script&family=Montserrat:wght@600;700;800&display=swap">
<style>
  :root {
    --backdrop: #e6e6e6;
    --paper: #f1eee8;
    --paper-warm: #efe3c8;
    --ink: #1c1a1a;
    --accent: #ef5438;
    --night: #1e0f3c;
    --white: #ffffff;
  }
  * { margin: 0; padding: 0; box-sizing: border-box; }
  html, body { width: 1200px; height: 1200px; overflow: hidden; }
  body {
    background: var(--backdrop);
    font-family: "Montserrat", sans-serif;
    position: relative;
  }
  .poster {
    position: absolute;
    left: 214px; top: 54px;
    width: 772px; height: 1091px;
    background:
      radial-gradient(ellipse 70% 40% at 10% 85%, var(--paper-warm), transparent 70%),
      var(--paper);
    overflow: hidden;
  }
  .hero-art {
    position: absolute;
    left: 0; top: 0;
    width: 772px; height: 600px;
    background:
      radial-gradient(ellipse 35% 25% at 50% 72%, #f2d8f0 0%, rgba(200,120,220,.6) 40%, transparent 75%),
      radial-gradient(ellipse 40% 35% at 8% 60%, #c9361f 0%, transparent 70%),
      radial-gradient(ellipse 35% 40% at 95% 70%, #d6411f 0%, transparent 70%),
      radial-gradient(ellipse 40% 30% at 90% 40%, #c4862a 0%, transparent 70%),
      radial-gradient(ellipse 50% 40% at 20% 20%, #5a6a2a 0%, transparent 70%),
      radial-gradient(ellipse 60% 40% at 60% 15%, #114a6a 0%, transparent 75%),
      linear-gradient(180deg, #1c3b5e 0%, #3f2f6a 55%, #5b1c24 100%);
    clip-path: polygon(0 92%, 12% 88%, 20% 96%, 32% 91%, 45% 98%, 58% 92%, 70% 97%, 84% 90%, 92% 95%, 100% 93%, 100% 0, 0 0);
  }
  .title {
    position: absolute;
    left: 0; width: 772px;
    text-align: center;
    color: var(--white);
  }
  .title-script {
    top: 40px;
    font-family: "Kaushan Script", cursive;
    font-size: 128px;
    line-height: 1.3;
  }
  .title-line1 {
    top: 262px;
    font-weight: 800;
    font-size: 58px;
    letter-spacing: 1px;
  }
  .title-line2 {
    top: 326px;
    font-weight: 800;
    font-size: 45px;
    letter-spacing: 1px;
  }
  .date-day {
    position: absolute;
    left: 166px; top: 614px;
    font-weight: 800;
    font-size: 45px;
    color: var(--ink);
    letter-spacing: -1px;
  }
  .date-year {
    position: absolute;
    left: 160px; top: 640px;
    font-weight: 700;
    font-size: 146px;
    line-height: 1.2;
    color: var(--accent);
    letter-spacing: -2px;
  }
  .time-badge {
    position: absolute;
    left: 534px; top: 621px;
    width: 63px; height: 150px;
    background: var(--night);
    border-radius: 0 12px 12px 0;
    display: flex; align-items: center; justify-content: center;
  }
  .time-badge span {
    transform: rotate(-90deg);
    white-space: nowrap;
    color: var(--white);
    font-weight: 800;
    font-size: 32px;
  }
  .rule {
    position: absolute;
    left: 107px; width: 545px;
    height: 1px; background: var(--ink);
  }
  .venue {
    position: absolute;
    left: 0; width: 772px; top: 798px;
    text-align: center;
    font-weight: 800;
    font-size: 45px;
    color: var(--ink);
    letter-spacing: -1px;
  }
  .address {
    position: absolute;
    left: 0; width: 772px; top: 850px;
    text-align: center;
    font-weight: 600;
    font-size: 21px;
    line-height: 28px;
    color: var(--ink);
  }
  .seating-label {
    position: absolute;
    left: 132px; top: 928px;
    font-weight: 800;
    color: var(--ink);
    line-height: 1;
    padding-right: 9px;
    border-right: 1px dotted var(--ink);
  }
  .seating-label .small { display: block; font-size: 18px; }
  .seating-label .big { display: block; font-size: 26px; margin-top: 2px; }
  .price-pill {
    position: absolute;
    top: 934px; height: 40px;
    display: flex;
    border-radius: 14px;
    overflow: hidden;
    font-weight: 800;
    color: var(--white);
  }
  .price-pill .amount {
    background: var(--night);
    width: 60px;
    display: flex; align-items: center; justify-content: center;
    font-size: 20px;
  }
  .price-pill .group {
    background: var(--accent);
    flex: 1;
    display: flex; align-items: center; justify-content: center;
    font-size: 15px;
    letter-spacing: .5px;
    border-left: 2px solid var(--white);
  }
  .pill-students { left: 280px; width: 174px; }
  .pill-adults { left: 463px; width: 175px; }
  .ticket-brand {
    position: absolute;
    left: 0; width: 772px; top: 996px;
    text-align: center;
    font-weight: 700;
    font-size: 27px;
    color: var(--accent);
    letter-spacing: -.5px;
  }
  .ticket-line {
    position: absolute;
    left: 0; width: 772px; top: 1030px;
    text-align: center;
    font-weight: 700;
    font-size: 19px;
    letter-spacing: 3px;
    color: var(--ink);
  }
  .ticket-line .label { color: var(--accent); margin-right: 6px; }
  .base-band {
    position: absolute;
    left: 0; bottom: 0;
    width: 772px; height: 13px;
    background: var(--night);
  }
</style>
</head>
<body>
  <main class="poster">
    <div class="hero-art" role="img" aria-label="Colourful watercolour backdrop with a cheering concert crowd silhouette and flowing music staff with notes"></div>

    <h1>
      <span class="title title-script">HarmoNest</span>
      <span class="title title-line1">ENSEMBLE</span>
      <span class="title title-line2">JUBILEE</span>
    </h1>

    <div class="date-day">SUNDAY OCT 2</div>
    <div class="date-year">2022</div>
    <div class="time-badge"><span>2-4 P.M</span></div>

    <div class="rule" style="top:789px"></div>
    <div class="venue">BRINDLE9 ALEHOUSE</div>
    <div class="address">Brindle9 Alehouse 413 Marlowe Ct<br>#200, Sacramento, CA 95821</div>
    <div class="rule" style="top:915px"></div>

    <div class="seating-label"><span class="small">GENERAL</span><span class="big">SEATING</span></div>
    <div class="price-pill pill-students"><span class="amount">$10</span><span class="group">STUDENTS</span></div>
    <div class="price-pill pill-adults"><span class="amount">$15</span><span class="group">ADULTS</span></div>

    <div class="ticket-brand">tixolvo</div>
    <div class="ticket-line"><span class="label">TICKETS:</span>www.Tixolvo.com</div>

    <div class="base-band"></div>
  </main>
</body>
</html>
```